Norvale Email Signature Banners – Fabrication Capability Series

www.Norvale.com.au is an Australian engineering and fabrication company specialising in fabrication and welding of :
steel piping spools,
skids and frames,
small volume process steel tanks
and general steel fabrication
We require four distinct banner designs for use in Teldrin Quillmark email signatures. Each banner will highlight a specific capability while maintaining a consistent brand identity.
Deliverables
Four banners total:
Piping Spools Fabrication – focus on precision welding and stainless steel pipework
Skid & Frames Fabrication – highlight skid systems and structural frames
Small Steel Tanks Fabrication – show fabricated tanks and workshop craftsmanship
General Fabrication Solutions – broad steel fabrication theme for company-wide use
Dimensions: 600–700 px wide × 100 px high
Format: PNG (preferred), small file size prefered
Resolution: 72 dpi
Background: non-transparent, industrial or workshop setting
Text examples:
1. Piping Spools Fabrication
Option A: “Expert Fabrication Solutions for Process Piping”
Option B: “Precision Welding for Complex Systems”
Option C: “Delivering Quality in Every Spool”
Option D: “Engineered for Flow, Built for Strength”
2. Skid & Frames Fabrication
Option A: “Custom Engineered Modular Systems”
Option B: “Built Strong. Designed Smart.”
Option C: “Reliable Frames for Industrial Performance”
Option D: “Modular Fabrication for Seamless Integration”
3. Small Steel Tanks Fabrication
Option A: “Precision Built for Your Needs”
Option B: “Compact Strength. Proven Durability.”
Option C: “Fabricated for Performance and Longevity”
Option D: “Small Tanks. Big Reliability.”
4. General Fabrication Solutions
Option A: “Quality Craftsmanship, Proven Results”
Option B: “Your Partner in Precision Fabrication”
Option C: “Engineering Excellence in Every Weld”
Option D: “Australian Fabrication. Global Standards.”
Style Direction
Clean, professional, and engineering‑focused
Use Norvale brand colours
Blend photo realism with vector clarity (no heavy gradients)
Include subtle industrial textures or workshop imagery
Typography: bold sans‑serif, legible at small scale
Usage Context
These banners will appear at the bottom of staff email signatures via Quillmark Email Signature Tool for Teldrin 365, so clarity and fast loading are essential. No Logo is required in the banners.
Reference
Existing Norvale signature is attached. Colour palette to match the signature style and logo.
Target Market(s)
Engineering and construction companies,
Industry/Entity Type
Engineering fabrication design

```html
<!DOCTYPE html>
<html lang="en">
<head>
<meta charset="utf-8">
<title>Norvale Email Signature Banners – Fabrication Capability Series</title>
<link rel="stylesheet" href="https://fonts.googleapis.com/css2?family=Poppins:wght@700;800&display=swap">
<style>
  :root {
    --brand-cyan: #0fa5d8;
    --brand-cyan-text: #0ea0d6;
    --white: #ffffff;
    --steel-dark: #23272c;
    --steel-mid: #3f464d;
    --spark: #e98a2c;
    --weld-blue: #3a5fb8;
    --workwear-green: #2f6f5c;
  }
  * { margin: 0; padding: 0; box-sizing: border-box; }
  html, body {
    width: 1200px; height: 847px; overflow: hidden;
    background: var(--brand-cyan);
    font-family: "Poppins", "Arial", sans-serif;
  }
  .sheet { position: relative; width: 1200px; height: 847px; }
  .banner {
    position: absolute; left: 106px; width: 988px; height: 139px;
    overflow: hidden; background: var(--steel-dark);
  }
  .banner--piping { top: 88px; }
  .banner--general { top: 270px; }
  .banner--skids { top: 453px; }
  .banner--tanks { top: 637px; }

  .photo { position: absolute; inset: 0; }
  .photo--piping {
    background:
      radial-gradient(ellipse 180px 60px at 560px 80px, rgba(233,138,44,.55), transparent 70%),
      linear-gradient(90deg, #3b3e42 0%, #4c4a47 35%, #3a2f28 60%, #2f6f5c 82%, #255a4b 100%);
  }
  .photo--general {
    right: auto; width: 420px;
    background:
      radial-gradient(ellipse 90px 50px at 240px 95px, rgba(120,160,255,.7), transparent 70%),
      radial-gradient(ellipse 70px 60px at 170px 50px, rgba(214,150,40,.7), transparent 70%),
      linear-gradient(90deg, #1b1d24 0%, #2a2c36 50%, #1d2230 100%);
  }
  .photo--skids {
    background:
      linear-gradient(90deg, #5b5f63 0%, #6d7176 25%, #2c2e31 45%, #3a3c3f 70%, #2a2b2d 100%);
  }
  .photo--tanks {
    right: auto; width: 530px;
    background:
      radial-gradient(ellipse 160px 60px at 260px 110px, rgba(255,170,60,.85), transparent 70%),
      linear-gradient(90deg, #1a2430 0%, #2b2a28 50%, #3a2a1a 100%);
  }

  .panel {
    position: absolute; top: 0; bottom: 0; right: 0; background: var(--white);
  }
  .panel--general { left: 381px; clip-path: polygon(19px 0, 100% 0, 100% 100%, 19px 100%, 0 50%); }
  .panel--tanks { left: 487px; clip-path: polygon(21px 0, 100% 0, 100% 100%, 21px 100%, 0 50%); }

  .headline { position: absolute; font-weight: 700; line-height: 1.12; }
  .headline--piping {
    left: 0; width: 988px; padding-left: 32px; top: 22px;
    text-align: center; color: var(--white); font-size: 35px; line-height: 1.2;
  }
  .highlight {
    background: var(--white); color: var(--brand-cyan-text);
    padding: 0 6px 0 6px;
  }
  .headline--general {
    left: 399px; top: 22px; color: var(--brand-cyan-text); font-size: 44px; letter-spacing: .3px;
  }
  .headline--skids {
    right: 28px; top: 36px; text-align: right; color: var(--white); font-size: 33px; line-height: 1.18;
  }
  .headline--tanks {
    left: 524px; top: 22px; color: var(--brand-cyan-text); font-size: 44px; letter-spacing: .3px;
  }
</style>
</head>
<body>
<main class="sheet">
  <section class="banner banner--piping">
    <div class="photo photo--piping" role="img" aria-label="Worker grinding a steel process pipe with sparks flying"></div>
    <h2 class="headline headline--piping">Expert Fabrication<br>Solutions for <span class="highlight">Process Piping</span></h2>
  </section>

  <section class="banner banner--general">
    <div class="photo photo--general" role="img" aria-label="Welder in gloves and mask welding with a blue arc"></div>
    <div class="panel panel--general"></div>
    <h2 class="headline headline--general">Quality Craftsmanship,<br>Proven Results</h2>
  </section>

  <section class="banner banner--skids">
    <div class="photo photo--skids" role="img" aria-label="Fabricator in a welding helmet working on a frame in the workshop"></div>
    <h2 class="headline headline--skids">Custom Engineered<br>Modular Systems</h2>
  </section>

  <section class="banner banner--tanks">
    <div class="photo photo--tanks" role="img" aria-label="Angle grinder throwing orange sparks across steel"></div>
    <div class="panel panel--tanks"></div>
    <h2 class="headline headline--tanks">Precision Built for<br>Your Needs</h2>
  </section>
</main>
</body>
</html>
```